Need Business Card for our Real Estate Business with Sales Executive's Picture

PANTONE 484 C ( RED)

PANTONE 2766 C ( BLUE

Industry/Entity Type

Real Estate

Contact Information for Business Card

Name, Mobile, email, & picture of Person
Agency Phone, address, Web address

Requirements
Must have
• Our Logo Colours, Agent Picture,

```html
<!DOCTYPE html>
<html lang="en">
<head>
<meta charset="utf-8">
<title>Dunmore Real Estate – Business Card</title>
<link href="https://fonts.googleapis.com/css2?family=Roboto:wght@400;500&display=swap" rel="stylesheet">
<style>
  :root {
    --navy: #0a1538;
    --brand-red: #9a3324;
    --paper: #f2f2f2;
    --white: #ffffff;
    --backdrop: #e8e5e0;
    --photo-top: #3a4f86;
    --photo-bottom: #1c2a55;
  }
  * { margin: 0; padding: 0; box-sizing: border-box; }
  html, body { width: 1200px; height: 960px; overflow: hidden; }
  body {
    position: relative;
    background: var(--backdrop);
    font-family: "Roboto", Arial, sans-serif;
  }
  .card {
    position: absolute;
    width: 600px;
    height: 343px;
    box-shadow: 0 2px 6px rgba(0,0,0,0.25);
  }
  .card-front { left: 314px; top: 113px; background: var(--paper); }
  .card-back { left: 311px; top: 472px; background: var(--navy); }

  .contact-panel {
    position: absolute; left: 0; top: 0;
    width: 256px; height: 100%;
    background: var(--navy);
    color: var(--white);
  }
  .accent-rule {
    position: absolute; left: 257px; top: 0;
    width: 3px; height: 100%;
    background: var(--brand-red);
  }
  .agent-photo {
    position: absolute; left: 37px; top: 34px;
    width: 84px; height: 100px;
    border-radius: 8px;
    border: 2px solid var(--white);
    background: linear-gradient(180deg, var(--photo-top), var(--photo-bottom));
  }
  .agent-name {
    position: absolute; left: 37px; top: 154px;
    font-size: 20px; font-weight: 500; letter-spacing: 0.2px;
  }
  .agent-title {
    position: absolute; left: 37px; top: 180px;
    font-size: 15px; font-weight: 400;
  }
  .address {
    position: absolute; left: 37px; top: 206px;
    font-size: 14.5px; line-height: 18px;
  }
  .contact-list {
    position: absolute; left: 37px; top: 246px;
    list-style: none;
    font-size: 14.5px;
  }
  .contact-list li {
    display: flex; align-items: center;
    height: 19px;
  }
  .contact-list svg { width: 13px; height: 13px; margin-right: 9px; fill: var(--white); }

  .brand {
    position: absolute;
    text-align: center;
    font-family: "Roboto", Arial, sans-serif;
    font-weight: 400;
  }
  .brand-name {
    display: flex; align-items: center; justify-content: center; gap: 12px;
    font-size: 44px; letter-spacing: 3px; line-height: 1;
  }
  .brand-tag {
    display: block; margin-top: 8px;
    font-size: 12px; letter-spacing: 2px;
  }
  .brand-mark {
    width: 12px; height: 12px;
    background: var(--brand-red);
  }
  .card-front .brand { left: 260px; width: 340px; top: 145px; color: var(--navy); }
  .card-back .brand { left: 0; width: 600px; top: 188px; color: var(--white); }
  .web-address {
    position: absolute; left: 0; width: 600px; top: 297px;
    text-align: center; color: var(--white);
    font-size: 14px; letter-spacing: 3.5px;
  }
</style>
</head>
<body>
  <section class="card card-front">
    <div class="contact-panel">
      <div class="agent-photo" role="img" aria-label="Portrait photo of the sales executive"></div>
      <h1 class="agent-name">DANIEL HARTLEY</h1>
      <p class="agent-title">CEO/FOUNDER</p>
      <p class="address">412 Willow Crest Road<br>Juneau, Alaska 99801</p>
      <ul class="contact-list">
        <li><svg viewBox="0 0 24 24"><path d="M6.6 10.8a15.1 15.1 0 0 0 6.6 6.6l2.2-2.2a1 1 0 0 1 1-.25 11.4 11.4 0 0 0 3.6.57 1 1 0 0 1 1 1V20a1 1 0 0 1-1 1A17 17 0 0 1 3 4a1 1 0 0 1 1-1h3.5a1 1 0 0 1 1 1c0 1.25.2 2.45.57 3.57a1 1 0 0 1-.25 1z"/></svg>907 555 0142</li>
        <li><svg viewBox="0 0 24 24"><path d="M7 1h10a2 2 0 0 1 2 2v18a2 2 0 0 1-2 2H7a2 2 0 0 1-2-2V3a2 2 0 0 1 2-2zm0 3v14h10V4zm5 15.5a1.2 1.2 0 1 0 0 2.4 1.2 1.2 0 0 0 0-2.4z"/></svg>907 555 0187</li>
        <li><svg viewBox="0 0 24 24"><path d="M2 5h20v14H2zm2 2v.5l8 5 8-5V7zm0 2.8V17h16V9.8l-8 5z"/></svg>daniel@dunmore.com</li>
        <li><svg viewBox="0 0 24 24"><path d="M12 2a10 10 0 1 0 0 20 10 10 0 0 0 0-20zm-1 17.9A8 8 0 0 1 4.2 10.6L9 15.4v1a2 2 0 0 0 2 2zm6.9-2.5a2 2 0 0 0-1.9-1.4h-1v-3a1 1 0 0 0-1-1H8v-2h2a1 1 0 0 0 1-1V7h2a2 2 0 0 0 2-2v-.4a8 8 0 0 1 2.9 12.8z"/></svg>www.dunmore.com</li>
      </ul>
    </div>
    <div class="accent-rule"></div>
    <div class="brand">
      <span class="brand-name"><span class="brand-mark"></span>DUNMORE</span>
      <span class="brand-tag">REAL ESTATE</span>
    </div>
  </section>

  <section class="card card-back">
    <div class="brand">
      <span class="brand-name"><span class="brand-mark"></span>DUNMORE</span>
      <span class="brand-tag">REAL ESTATE</span>
    </div>
    <p class="web-address">www.dunmore.com</p>
  </section>
</body>
</html>
```